Business Card Design for general contractor or developer

General Contractors. We build new buildings as well as redesign and/or remodel existing buildings. Mostly residential, but we want to expand to commercial as well, so we want the design not to be residential specific.We want the design to be modern, but necessarily minimalistic. A monogram type is also a consideration, but would like to see all ideas.

Target Market(s)

Real estate investors, homeowners, future homeowners, commercial building owners

Industry/Entity Type

Contractor

Contact Information for Business Card

BRIMCOVE Developers Corp, 6127 NE 318th Avenue Suite 241 Miami Lakes, FL 33482, Curtis Ortega, (305) 472-1803, curtis@quarvinta.com

Font styles to use
Other font styles liked:
• Modern type font

Requirements
Must have
• Must be modern looking
Nice to have
• Metallic type or a standout feature
Should not have
• Tools, floorplans

```html
<!DOCTYPE html>
<html lang="en">
<head>
<meta charset="utf-8">
<title>BRIMCOVE Developers Corp – Business Card</title>
<link href="https://fonts.googleapis.com/css2?family=Didact+Gothic&display=swap" rel="stylesheet">
<style>
  :root {
    --backdrop: #e9e6e1;
    --card-black: #0b0c0d;
    --card-black-soft: #16181a;
    --metal-light: #7d8386;
    --metal-mid: #4c5254;
    --metal-dark: #2a2e30;
    --ink-white: #f2f4f5;
    --ink-teal: #14302f;
    --ring-grey: #3a3f42;
    --drawing-grey: #8a9094;
  }
  * { margin: 0; padding: 0; box-sizing: border-box; }
  html, body {
    width: 1200px;
    height: 675px;
    overflow: hidden;
    background: var(--backdrop);
    font-family: "Didact Gothic", "Century Gothic", sans-serif;
  }
  .stage {
    position: relative;
    width: 1200px;
    height: 675px;
    display: flex;
    align-items: center;
    justify-content: center;
    gap: 40px;
  }
  .card {
    position: relative;
    width: 540px;
    height: 309px;
    overflow: hidden;
    box-shadow: 0 10px 28px rgba(0, 0, 0, 0.28);
  }

  /* Back face */
  .card-back {
    background: radial-gradient(ellipse at 40% 40%, var(--card-black-soft), var(--card-black) 70%);
  }
  .emblem-ring {
    position: absolute;
    left: 170px;
    top: 40px;
    width: 200px;
    height: 200px;
  }
  .emblem-drawing {
    position: absolute;
    left: 208px;
    top: 82px;
    width: 124px;
    height: 112px;
    background: radial-gradient(ellipse at 50% 55%, #5a6064, #22272a 75%);
    border-radius: 6px;
  }

  /* Front face */
  .card-front {
    background: var(--card-black);
  }
  .front-top {
    position: absolute;
    inset: 0 0 auto 0;
    height: 172px;
    background: linear-gradient(180deg, #0d0f10, var(--card-black));
  }
  .front-metal {
    position: absolute;
    inset: 172px 0 0 0;
    background:
      repeating-linear-gradient(180deg, rgba(255,255,255,0.05) 0 1px, rgba(0,0,0,0.05) 1px 3px),
      linear-gradient(100deg, var(--metal-dark) 0%, var(--metal-mid) 25%, var(--metal-light) 55%, var(--metal-mid) 80%, var(--metal-dark) 100%);
  }
  .house-drawing {
    position: absolute;
    left: 228px;
    top: 44px;
    width: 150px;
    height: 96px;
    background: linear-gradient(180deg, #4b5155, #1e2225);
    border-radius: 4px;
  }
  .company-name {
    position: absolute;
    left: 0;
    right: 0;
    top: 146px;
    text-align: center;
    padding-left: 40px;
    font-size: 25px;
    letter-spacing: 0.5px;
    color: var(--ink-white);
    text-shadow: 0 1px 2px rgba(0, 0, 0, 0.6);
  }
  .contact {
    position: absolute;
    left: 0;
    right: 0;
    top: 188px;
    text-align: center;
    padding-left: 70px;
    font-size: 12.5px;
    line-height: 17px;
    color: var(--ink-teal);
  }
  .contact .person-line {
    margin-left: -110px;
  }
</style>
</head>
<body>
  <main class="stage">
    <section class="card card-back" aria-label="Card back">
      <svg class="emblem-ring" viewBox="0 0 200 200" aria-hidden="true">
        <circle cx="100" cy="100" r="88" fill="none" stroke="var(--ring-grey)" stroke-width="12"/>
      </svg>
      <div class="emblem-drawing" role="img" aria-label="Line drawing of a two-storey house with gabled roofs"></div>
    </section>

    <section class="card card-front" aria-label="Card front">
      <div class="front-top"></div>
      <div class="front-metal"></div>
      <div class="house-drawing" role="img" aria-label="Line drawing of a two-storey house with gabled roofs"></div>
      <h1 class="company-name">BRIMCOVE Developers Corp</h1>
      <address class="contact" style="font-style: normal;">
        <div class="address-line">6127 NE 318th Avenue Suite</div>
        <div class="address-line">241 Miami Lakes, FL 33482,</div>
        <div class="person-line">Curtis Ortega, (305) 472-1803, curtis@quarvinta.com</div>
      </address>
    </section>
  </main>
</body>
</html>
```